Luxury Customizable Mattress Company Needs a Business Card that WOWs

I need a unique business card design that makes people stop... look and think WOW.

We are a new mattress company with our very own line of customizable beds (mattress & base) called the Trellis Rest. The innovation of our mattress is that the entire product is built of smaller components... once put together its a complete bed. It can be cleaned from the inside out. And it's a mattress made to share with a partner. As people's sleep needs are different, one person may prefer a water bed and a softer mattress while their partner may prefer a warm memory foam mattress with a firmer feel. Now they dont need to compromise, as the Trellis Rest allows each sleeper to get exactly what they need. And they can each change the feel of their side of the bed anytime with a click of a button.
check www.Trellisrest.example for more info (some pages do not work) Also check out our Clipora and Streamly videos.

We also opened up a new facility where people can try out our beds... called the Doze Harbor. This is a secondary business but we would like to have a small logo on the TR business card to highlight it. (dozeharbor.example)

Content on card....
Logo: Trellis Rest logo
Name: Miriam Okafor
Title: CEO & Sleep Enthusiast
Address: 4829 Varley Crescent Mississauga ON L5R 2T6 Canada
Telephone: 416.555.0193 (place holder .. this # will change)
Email: miriam@trellisrest.example
Web: www.trellisrest.example

Small Logo: Doze Harbor Logo
web: dozeharbor.example

Design: bold and modern, the design has a concept, if possible a card people can use (to ensure they keep the card) Ie. Sleep positions or NFC chip or something interesting. I am open to ideas and printing on unique materials... like soft vinyl fabric.

Target Market(s)

Mattress Consumers
Married Couples
Couples

Industry/Entity Type

Health And Wellness

Contact Information for Business Card

Logo: Trellis Rest logo
Name: Miriam Okafor
Web: www.trellisrest.example

SMALL Logo: Doze Harbor Logo
web: dozeharbor.example

Requirements
Must have
• bold and modern, the design has a concept, if possible a card people can use (to ensure they keep the card)
• ** I LIKE THIS CONCEPT: http://plovix.example/wp-content/uploads/2014/04/beautiful-creative-unique-original-impressive-business-cards-designs-18.jpg
• And the DESIGN I thought of has a silhouette of a woman sleeping on top of front of card and if you flip the card over there's a silhouette of a man sleeping on the bottom of the back of the card. IF you put 2 cards together (back to front) it looks like they are sleeping together.
• INSIDE pull out card can be designed later.
• See our website and videos for images we've used in the past.
• We are open to new concepts, images, stories.
• Must be story / people driven. Mattress sales are driven by the idea of good sleep, solving sleep issues and making people happy.
Nice to have
• Just some examples.... adding a feature to the card like a Sleep positions chart or NFC chip or something interesting. I am open to ideas and printing on unique materials... like soft vinyl fabric.
Should not have
• not dull in colour or concept

```html
<!DOCTYPE html>
<html lang="en">
<head>
<meta charset="utf-8">
<title>Trellis Rest – Business Card</title>
<link href="https://fonts.googleapis.com/css2?family=Exo+2:wght@500;600;700&family=Arimo:wght@400;700&display=swap" rel="stylesheet">
<style>
  :root {
    --bg: #ece9e4;
    --paper: #ffffff;
    --ink: #0b0b0b;
    --brand-blue: #1a8fd6;
    --brand-cyan: #1fb6e8;
    --navy: #2c3e9a;
    --grey: #9a9a9a;
    --text-light: #e9e9e9;
    --shadow: rgba(0,0,0,0.22);
  }
  * { margin: 0; padding: 0; box-sizing: border-box; }
  html, body { width: 1200px; height: 892px; overflow: hidden; background: var(--bg); }
  body { position: relative; font-family: "Arimo", Arial, sans-serif; }

  .card {
    position: absolute;
    background: var(--paper);
    box-shadow: 0 10px 28px var(--shadow);
    overflow: hidden;
  }

  /* Front: vertical card */
  .card--front { left: 110px; top: 149px; width: 340px; height: 594px; }
  .front__wave { position: absolute; left: 0; top: 0; width: 340px; height: 594px; }
  .front__brand {
    position: absolute; top: 120px; left: 0; width: 100%;
    display: flex; flex-direction: column; align-items: center; gap: 18px;
  }
  .brand__mark { width: 46px; height: 46px; background: var(--brand-blue); border-radius: 6px; }
  .brand__name {
    font-family: "Exo 2", sans-serif; font-weight: 600; font-size: 34px;
    letter-spacing: 4px; color: var(--navy); text-transform: uppercase;
  }
  .front__person {
    position: absolute; left: 28px; top: 380px; right: 20px;
  }
  .person__name {
    font-family: "Exo 2", sans-serif; font-weight: 700; font-size: 33px;
    color: var(--brand-cyan); line-height: 1.05;
  }
  .person__title {
    font-family: "Exo 2", sans-serif; font-weight: 500; font-size: 19px;
    color: var(--text-light); margin-top: 4px;
  }
  .person__contact {
    list-style: none; margin-top: 24px; color: var(--text-light);
    font-size: 15px; line-height: 1.5;
  }

  /* Back: horizontal card */
  .card--back { left: 520px; top: 276px; width: 594px; height: 340px;
    background: linear-gradient(160deg, #ffffff 40%, #f1f3f5 100%); }
  .back__inner {
    position: absolute; inset: 0; display: flex; align-items: center;
    padding: 0 56px; gap: 44px;
  }
  .back__text { display: flex; flex-direction: column; }
  .sub__name {
    font-family: "Exo 2", sans-serif; font-weight: 700; font-size: 38px;
    letter-spacing: 6px; color: var(--brand-blue); text-transform: uppercase;
  }
  .sub__by { font-size: 13px; color: var(--brand-blue); margin-top: 2px; align-self: flex-end; }
  .sub__web { font-weight: 700; font-size: 22px; color: var(--brand-blue); margin-top: 18px; }
  .sub__mark {
    flex: none; width: 170px; height: 170px; border-radius: 50%;
    background: radial-gradient(circle at 40% 35%, #2aa6ea, #1479c4);
  }
</style>
</head>
<body>

<section class="card card--front" aria-label="Business card front">
  <svg class="front__wave" viewBox="0 0 340 594" aria-hidden="true">
    <path d="M0 330 C 60 370, 150 395, 230 385 C 285 378, 320 370, 340 372 L340 594 L0 594 Z" fill="var(--ink)"/>
    <path d="M0 330 C 60 370, 150 395, 230 385 C 285 378, 320 370, 340 372" fill="none" stroke="var(--brand-blue)" stroke-width="7"/>
  </svg>

  <div class="front__brand">
    <span class="brand__mark"></span>
    <span class="brand__name">Trellis Rest</span>
  </div>

  <div class="front__person">
    <h1 class="person__name">Miriam Okafor</h1>
    <p class="person__title">CEO &amp; Sleep Enthusiast</p>
    <ul class="person__contact">
      <li>416.555.0193</li>
      <li>www.trellisrest.example</li>
      <li>miriam@trellisrest.example</li>
      <li>4829 Varley Crescent Mississauga</li>
      <li>ON L5R 2T6 Canada</li>
    </ul>
  </div>
</section>

<section class="card card--back" aria-label="Business card back">
  <div class="back__inner">
    <div class="back__text">
      <span class="sub__name">Doze Harbor</span>
      <span class="sub__by">by Trellis Rest</span>
      <span class="sub__web">dozeharbor.example</span>
    </div>
    <span class="sub__mark"></span>
  </div>
</section>

</body>
</html>
```